Tavor Management - Managing Urban Projects for the City of Modiin

Tavor Management needs a website that projects its professionalism and innovation to the residents of the city of Modiin. The design needs include: 1) a homepage design, 2) ~12 customized icons used on the homepage, 3) a layered image (city landscape with company logo on it) used as a fullwidth background image on the homepage. The client wants a site that is pleasant on the eye and easy to navigate. The client wants the site to project the organization as being professional and innovative.

Target Market(s)

adult residents of the city of modiin, israel

Industry/Entity Type

management of urban projects

Number of Pages Required

1 page

Font styles to use
Sans Serif

Requirements
Must have
• psd of design and psd of main fullwidth background image on the homepage
Nice to have
• icons for navigation bar and homepage teasers
Should not have
• colors should match the logo attached, font should be modern

```html
<!DOCTYPE html>
<html lang="en">
<head>
<meta charset="utf-8">
<title>Tavor Management</title>
<link href="https://fonts.googleapis.com/css2?family=Oswald:wght@500;600;700&family=Poppins:wght@400;500;600&display=swap" rel="stylesheet">
<style>
:root{
  --green:#5aa64b;
  --green-dark:#2e7d32;
  --green-deep:#1f6b2a;
  --ink:#333;
  --muted:#777;
  --panel:#f1f1f1;
  --frame:#d9d9d9;
  --footer:#2f2f2f;
  --white:#fff;
}
*{box-sizing:border-box;margin:0;padding:0}
html,body{width:1200px;height:2818px;overflow:hidden}
body{position:relative;font-family:'Poppins',sans-serif;color:var(--ink);background:var(--white)}
.abs{position:absolute}
.heading{font-family:'Oswald',sans-serif;font-weight:700;color:#2b2b2b;text-transform:uppercase;letter-spacing:.5px}

/* hero */
.hero{left:0;top:0;width:1200px;height:569px;background:linear-gradient(180deg,#9fb3c4 0%,#8a9aa3 25%,#7f8a82 55%,#6b7564 100%)}
.brand-badge{left:520px;top:27px;width:160px;height:160px;border-radius:50%;background:var(--white);display:flex;align-items:center;justify-content:center;text-align:center;font-weight:600;font-size:15px;color:var(--green-dark);line-height:1.3;z-index:2}
.side-nav{left:1037px;top:0;width:163px;height:568px;display:flex;flex-direction:column;z-index:2}
.side-nav .item{display:flex;border-bottom:1px solid rgba(255,255,255,.15)}
.side-nav .label{width:112px;background:var(--green);color:var(--white);font-size:11.5px;font-weight:500;text-align:center;display:flex;align-items:center;justify-content:center;line-height:1.25;padding:0 6px}
.side-nav .icon{width:51px;background:var(--green-dark);display:flex;align-items:center;justify-content:center}
.side-nav svg{width:32px;height:32px;stroke:var(--white);fill:none;stroke-width:2}
.teaser{top:416px;width:202px;height:188px;border:4px solid var(--white);border-radius:10px;color:var(--white);display:flex;flex-direction:column;align-items:center;justify-content:center;text-align:center;font-size:12.5px;line-height:1.35;padding:0 20px;z-index:3}
.teaser.light{background:var(--green)}
.teaser.dark{background:var(--green-dark)}
.teaser svg{width:72px;height:60px;stroke:var(--white);fill:none;stroke-width:2;margin-bottom:14px}

/* about */
.about{left:0;top:569px;width:1200px;height:689px;background:var(--panel)}
.mark{display:flex;align-items:center;gap:8px;font-weight:600;font-size:15px;color:var(--green-dark);left:0;width:1200px;justify-content:center}
.mark .dot{width:14px;height:14px;border-radius:50%;background:var(--green)}
.frame-top{height:6px;background:var(--frame)}
.frame-side{width:6px;background:var(--frame)}
.dots{background-image:radial-gradient(#c9c9c9 1.6px,transparent 1.8px);background-size:14px 14px}
.bar{background:var(--green)}
.photo{border-radius:4px}
.sub-title{font-family:'Oswald',sans-serif;font-weight:600;font-size:22px;color:#333;text-transform:uppercase}
.copy{font-size:12.5px;line-height:16.5px;color:var(--muted)}
.checks{list-style:none;font-size:12.5px;color:var(--muted)}
.checks li{display:flex;align-items:center;gap:8px;height:23.5px}
.checks svg{width:14px;height:14px}
.btn{display:flex;align-items:center;justify-content:center;gap:10px;font-weight:600;font-size:13.5px;color:var(--white);background:var(--green);border-radius:5px;text-transform:uppercase}
.btn svg{width:14px;height:14px}

/* projects */
.proj-left{left:0;top:1258px;width:627px;height:496px;background:var(--green)}
.proj-right{left:627px;top:1258px;width:573px;height:496px;background:linear-gradient(160deg,#c9d5d2,#b8c8c0 50%,#a9bcae)}
.proj-frame-top{left:77px;top:1313px;width:303px;height:7px;background:#7cc26a}
.proj-frame-side{left:77px;top:1313px;width:7px;height:297px;background:#7cc26a}
.proj-card{top:1317px;width:274px;height:359px;border:8px solid var(--white);border-radius:30px;box-shadow:0 4px 12px rgba(0,0,0,.12)}
.arrow-btn{top:1694px;width:30px;height:26px;border:1.5px solid #555;border-radius:4px;display:flex;align-items:center;justify-content:center;background:rgba(255,255,255,.3)}
.arrow-btn svg{width:12px;height:12px;stroke:#333;fill:none;stroke-width:2}

/* contact */
.field-label{font-size:12.5px;color:var(--muted)}
.field{border:1px solid #dcdcdc;background:var(--white)}

/* footer */
.footer{left:0;top:2508px;width:1200px;height:254px;background:var(--footer)}
.foot-head{font-family:'Oswald',sans-serif;font-weight:500;font-size:20px;color:var(--white);text-transform:uppercase}
.foot-text{font-size:11.5px;line-height:16.5px;color:#ddd}
.links{list-style:none;font-size:11.5px;color:#ddd}
.links li{height:23.5px;display:flex;align-items:center;gap:7px}
.links li::before{content:"»";color:#ddd;font-size:12px}
.contact-line{display:flex;align-items:center;gap:9px;font-size:11.5px;color:#ddd;height:25px}
.contact-line svg{width:13px;height:13px;fill:#ddd}
.social{width:28px;height:28px;border:1.5px solid #ddd;border-radius:50%}
.to-top{left:1122px;top:2677px;width:32px;height:32px;border-radius:50%;background:#555;display:flex;align-items:center;justify-content:center}
.copyright{left:0;top:2762px;width:1200px;height:56px;background:var(--green);color:var(--white);font-size:15px;display:flex;align-items:center;justify-content:center}
</style>
</head>
<body>

<!-- hero -->
<div class="abs hero" role="img" aria-label="Aerial view of a city business district with glass office buildings and tree-lined roads"></div>
<div class="abs brand-badge">Tavor<br>Management</div>

<nav class="abs side-nav">
  <div class="item" style="height:80px"><div class="label">HOME</div><div class="icon"><svg viewBox="0 0 32 32"><path d="M4 16 16 5l12 11M8 13v14h16V13M13 27v-8h6v8"/></svg></div></div>
  <div class="item" style="height:76px"><div class="label">COMPANY PROFILE</div><div class="icon"><svg viewBox="0 0 32 32"><rect x="6" y="4" width="20" height="18"/><circle cx="16" cy="11" r="3"/><path d="M11 18h10M12 26h8M16 22v4"/></svg></div></div>
  <div class="item" style="height:75px"><div class="label">PROJECTS</div><div class="icon"><svg viewBox="0 0 32 32"><path d="M5 27h22M8 27V12h6v15M14 27V6h8v21M17 10h2M17 14h2M17 18h2M10 16h2M10 20h2"/></svg></div></div>
  <div class="item" style="height:83px"><div class="label">MANAGEMENT AND MAINTENANCE</div><div class="icon"><svg viewBox="0 0 32 32"><rect x="4" y="6" width="24" height="20"/><circle cx="16" cy="16" r="5"/><path d="M16 9v2M16 21v2M9 16h2M21 16h2"/></svg></div></div>
  <div class="item" style="height:70px"><div class="label">TENDERS</div><div class="icon"><svg viewBox="0 0 32 32"><path d="M6 4h14v24H6zM9 10h8M9 14h8M9 18h5M28 8 17 21l-2 4 4-2L30 10z"/></svg></div></div>
  <div class="item" style="height:81px"><div class="label">PHOTOS<br>AND VIDEOS</div><div class="icon"><svg viewBox="0 0 32 32"><rect x="3" y="4" width="14" height="12"/><rect x="13" y="14" width="16" height="13"/><path d="M15 25l5-5 4 4 3-2"/></svg></div></div>
  <div class="item" style="height:103px;border:0"><div class="label">CONTACT</div><div class="icon"><svg viewBox="0 0 32 32"><path d="M10 5h18v13h-6l-4 4v-4h-8zM4 12h4v9h6v4l-4-4H4z"/></svg></div></div>
</nav>

<!-- about background (drawn before teasers so they sit on top) -->
<section class="abs about"></section>

<div class="abs teaser light" style="left:162px"><svg viewBox="0 0 72 60"><path d="M4 12h36v30H4zM40 24h14l10 10v8H40M18 48a5 5 0 1 0 0-1M52 48a5 5 0 1 0 0-1"/></svg>THE TRANSPORTATION CENTER</div>
<div class="abs teaser dark" style="left:382px"><svg viewBox="0 0 72 60"><path d="M10 18 36 4l26 14zM12 18h48M16 22v26M26 22v26M46 22v26M56 22v26M8 50h56M6 56h60M30 48V30h12v18"/></svg>THE MUNICIPAL SPORTS CENTER</div>
<div class="abs teaser light" style="left:602px"><svg viewBox="0 0 72 60"><circle cx="44" cy="18" r="12"/><path d="M44 30v24M38 44l6-4 6 4M10 44h22v4H10zM14 48v6M28 48v6M20 14l4-2M14 22l4-2"/></svg>CEDAR PARK</div>
<div class="abs teaser dark" style="left:822px"><svg viewBox="0 0 72 60"><path d="M8 56V26l12-12 12 12v30M14 40h12M14 48h12M32 34h8v22M40 34l10 0 8 16h8"/><circle cx="20" cy="30" r="4"/></svg>THE TECHNOLOGY PARK</div>

<!-- about -->
<div class="abs mark" style="top:665px"><span class="dot"></span>Tavor Management</div>
<h2 class="abs heading" style="left:0;width:1200px;top:722px;text-align:center;font-size:54px;line-height:1.2">About Us</h2>
<div class="abs frame-top" style="left:829px;top:708px;width:301px"></div>
<div class="abs frame-side" style="left:1124px;top:708px;height:334px"></div>
<div class="abs dots" style="left:106px;top:782px;width:144px;height:116px"></div>
<div class="abs bar" style="left:148px;top:892px;width:12px;height:200px"></div>
<div class="abs photo" style="left:162px;top:832px;width:247px;height:347px;background:linear-gradient(160deg,#7a9a5e,#8a7d66 50%,#9a8f7f)" role="img" aria-label="Father and young son walking hand in hand in a garden"></div>
<div class="abs photo" style="left:420px;top:832px;width:175px;height:171px;background:linear-gradient(180deg,#7e8fa8,#a99473 70%,#5b6470)" role="img" aria-label="Modern public building entrance at dusk"></div>
<div class="abs photo" style="left:420px;top:1014px;width:175px;height:164px;background:linear-gradient(180deg,#c6b690,#a99670 60%,#857455)" role="img" aria-label="Aerial view of a transportation hub with buses and palm trees"></div>
<h3 class="abs sub-title" style="left:620px;top:834px">Sorem Ipsum Dolor Sit Amet</h3>
<p class="abs copy" style="left:620px;top:879px;width:415px">Lorem ipsum dolor sit amet, consectetur adipiscing elit. Vestibulum quis diam in tortor auctor egestas. Sed et felis at augue laoreet blandit nec vitae libero. Nam vitae enim commodo, congue turpis at, dapibus justo. Morbi pharetra, elit ac mollis fringilla, quam diam rhoncus libero, sollicitudin molestie est quam in sapien. Lorem ipsum dolor sit amet, consectetur adipiscing elit. Vestibulum quis diam in tortor auctor egestas. Sed et felis at augue laoreet blandit nec vitae libero. Nam vitae enim commodo, congue turpis at.</p>
<ul class="abs checks" style="left:620px;top:1033px">
  <li><svg viewBox="0 0 14 14"><circle cx="7" cy="7" r="7" fill="#5aa64b"/><path d="M4 7.2l2 2 4-4" stroke="#fff" stroke-width="1.6" fill="none"/></svg>Lorem ipsum dolor sit amet, consectetur adipiscing elit.</li>
  <li><svg viewBox="0 0 14 14"><circle cx="7" cy="7" r="7" fill="#5aa64b"/><path d="M4 7.2l2 2 4-4" stroke="#fff" stroke-width="1.6" fill="none"/></svg>Curabitur sed nisi ultrices, dignissim nulla et, facilisis neque.</li>
  <li><svg viewBox="0 0 14 14"><circle cx="7" cy="7" r="7" fill="#5aa64b"/><path d="M4 7.2l2 2 4-4" stroke="#fff" stroke-width="1.6" fill="none"/></svg>Fusce porta orci vitae tortor tincidunt sit amet .</li>
</ul>
<div class="abs btn" style="left:620px;top:1125px;width:134px;height:40px">About Us <svg viewBox="0 0 14 14"><circle cx="7" cy="7" r="7" fill="#fff"/><path d="M6 4l3 3-3 3" stroke="#5aa64b" stroke-width="1.8" fill="none"/></svg></div>

<!-- projects -->
<div class="abs proj-left"></div>
<div class="abs proj-right" role="img" aria-label="Faded city skyline background"></div>
<div class="abs proj-frame-top"></div>
<div class="abs proj-frame-side"></div>
<h2 class="abs heading" style="left:161px;top:1372px;font-size:42px;color:var(--white);line-height:1.2">Our Project</h2>
<p class="abs copy" style="left:161px;top:1444px;width:300px;color:var(--white)">Lorem ipsum dolor sit amet, consectetur adipiscing elit. Vestibulum quis diam in tortor auctor egestas. Sed et felis at augue laoreet blandit nec vitae libero. Nam vitae enim commodo, congue turpis at, dapibus justo. Morbi pharetra, elit ac mollis fringilla, quam diam rhoncus libero, sollicitudin molestie est quam in sapien. Lorem ipsum dolor sit amet.</p>
<div class="abs btn" style="left:161px;top:1599px;width:136px;height:43px;background:transparent;border:2px solid var(--white)">View More <svg viewBox="0 0 14 14"><circle cx="7" cy="7" r="7" fill="#fff"/><path d="M6 4l3 3-3 3" stroke="#5aa64b" stroke-width="1.8" fill="none"/></svg></div>
<div class="abs bar" style="left:1037px;top:1395px;width:13px;height:202px"></div>
<div class="abs proj-card" style="left:474px;background:linear-gradient(180deg,#4c5a72,#6d6a60 45%,#8c7a58 75%,#3d6f8f)" role="img" aria-label="City interchange with light trails at night"></div>
<div class="abs proj-card" style="left:764px;background:linear-gradient(180deg,#8a7a63,#6f7c8a 40%,#3c4346 75%,#2c3032)" role="img" aria-label="Entrance of the transportation center building"></div>
<div class="abs arrow-btn" style="left:720px"><svg viewBox="0 0 12 12"><path d="M8 2 4 6l4 4"/></svg></div>
<div class="abs arrow-btn" style="left:755px;border-color:var(--green)"><svg viewBox="0 0 12 12" style="stroke:var(--green)"><path d="M4 2l4 4-4 4"/></svg></div>

<!-- contact -->
<div class="abs mark" style="top:1820px"><span class="dot"></span>Tavor Management</div>
<p class="abs" style="left:0;width:1200px;top:1876px;text-align:center;font-weight:600;font-size:17px;color:var(--green-dark)">GET IN TOUCH</p>
<h2 class="abs heading" style="left:0;width:1200px;top:1895px;text-align:center;font-size:54px;line-height:1.2">Contact Us</h2>
<div class="abs frame-top" style="left:829px;top:1887px;width:301px"></div>
<div class="abs frame-side" style="left:1124px;top:1887px;height:334px"></div>
<div class="abs dots" style="left:106px;top:1970px;width:144px;height:116px"></div>
<div class="abs bar" style="left:142px;top:2071px;width:14px;height:286px"></div>
<div class="abs" style="left:162px;top:1997px;width:418px;height:440px;border:6px solid var(--white);border-radius:30px;box-shadow:0 4px 12px rgba(0,0,0,.15);background:linear-gradient(180deg,#6f7c82,#4e6a5a 35%,#3f6a3c 60%,#8e8578)" role="img" aria-label="Aerial view of a park playground with a fountain and shade sails at dusk"></div>
<p class="abs copy" style="left:620px;top:2018px;width:420px">Lorem ipsum dolor sit amet, consectetur adipiscing elit. Vestibulum quis diam in tortor auctor egestas. Sed et felis at augue laoreet blandit nec vitae libero.</p>
<span class="abs field-label" style="left:620px;top:2084px">Name</span>
<span class="abs field-label" style="left:834px;top:2084px">Phone</span>
<div class="abs field" style="left:620px;top:2106px;width:204px;height:40px"></div>
<div class="abs field" style="left:834px;top:2106px;width:204px;height:40px"></div>
<span class="abs field-label" style="left:620px;top:2160px">Email</span>
<div class="abs field" style="left:620px;top:2182px;width:418px;height:40px"></div>
<span class="abs field-label" style="left:620px;top:2236px">Message</span>
<div class="abs field" style="left:620px;top:2258px;width:418px;height:78px"></div>
<div class="abs btn" style="left:620px;top:2355px;width:133px;height:40px">Submit <svg viewBox="0 0 14 14"><circle cx="7" cy="7" r="7" fill="#fff"/><path d="M6 4l3 3-3 3" stroke="#5aa64b" stroke-width="1.8" fill="none"/></svg></div>

<!-- footer -->
<footer class="abs footer"></footer>
<h4 class="abs foot-head" style="left:161px;top:2553px">About Us</h4>
<p class="abs foot-text" style="left:161px;top:2596px;width:265px">Lorem ipsum dolor sit amet, consectetur adipiscing elit. Vestibulum quis diam in tortor auctor egestas. Sed et felis at augue laoreet blandit nec vitae libero. Nam vitae enim commodo, congue turpis at.</p>
<div class="abs btn" style="left:164px;top:2693px;width:114px;height:30px;font-size:11.5px">Read More <svg viewBox="0 0 14 14"><circle cx="7" cy="7" r="7" fill="#fff"/><path d="M6 4l3 3-3 3" stroke="#5aa64b" stroke-width="1.8" fill="none"/></svg></div>

<h4 class="abs foot-head" style="left:465px;top:2553px">Quick Links</h4>
<ul class="abs links" style="left:465px;top:2593px">
  <li>Home</li><li>About</li><li>Business Promotion</li><li>Project Management</li><li>Tech and Commercial Areas</li>
</ul>
<ul class="abs links" style="left:660px;top:2593px">
  <li>Tenders</li><li>Signage and Publication</li><li>Projects</li><li>Contact</li>
</ul>

<h4 class="abs foot-head" style="left:852px;top:2553px">Contact Details</h4>
<div class="abs" style="left:852px;top:2593px">
  <div class="contact-line"><svg viewBox="0 0 14 14"><path d="M7 0a5 5 0 0 0-5 5c0 4 5 9 5 9s5-5 5-9a5 5 0 0 0-5-5zm0 7a2 2 0 1 1 0-4 2 2 0 0 1 0 4z"/></svg>Harvest Lane 12</div>
  <div class="contact-line"><svg viewBox="0 0 14 14"><path d="M3 1l2 0 1 3-1.5 1.2a8 8 0 0 0 4.3 4.3L10 8l3 1v2c0 1-1 2-2 2C6 13 1 8 1 3c0-1 1-2 2-2z"/></svg>+ 08-5550142</div>
  <div class="contact-line"><svg viewBox="0 0 14 14"><path d="M3 1h8v4H3zM1 5h12v6h-2v2H3v-2H1zm3 4v3h6V9z"/></svg>Fax: 08-5550143</div>
</div>
<div class="abs social" style="left:853px;top:2679px"></div>
<div class="abs social" style="left:889px;top:2679px"></div>
<div class="abs social" style="left:925px;top:2679px"></div>
<div class="abs to-top"><svg viewBox="0 0 12 12" width="12" height="12"><path d="M2 8l4-4 4 4" stroke="#ddd" stroke-width="1.8" fill="none"/></svg></div>

<div class="abs copyright">© 2024 Tavor Management | All Right Reserved.</div>

</body>
</html>
```